Marlo’s Sandwich Corner Grand Opening Door Flyer

1. Project Title
• “Flyer Design for Sandwich Shop Grand Opening”
• Why it’s effective: Direct and to the point, highlighting the purpose of the design.

2. Project Description
• “We’re looking for a professional designer to create a vibrant and modern flyer for our sandwich shop, Marlo’s Corner. The flyer should emphasize our handcrafted sandwiches, fresh-baked bread, and house-made meats. As a women & family-owned business, we want this aspect prominently displayed. The flyer should also include our logo, a ‘Grand Opening’ and our website: MarlosCorner.com. We want the design to be clean, bold, and visually appealing to attract customers. We also would like a QR code so they can scan to load of the website to order online, but also list it.
• Why it’s effective: Clear goals, modern style preference, and necessary details outlined.

3. Visual Style
• “Modern, bold, and clean design with bright, appetizing colors. Focus on high-quality imagery of sandwiches, sleek fonts, and an inviting layout.”
• Why it’s effective: Communicates the desired aesthetic and tone.

4. Key Details to Include
• Business Name: Marlo’s Sandwich Corner
• Taglines:
“Women & Family Owned”
“Handcrafted Sandwiches Made with Love”
“Fresh Baked Bread”
“House-made Slow Roasted House Specialties”
“Gluten-Friendly”
“Vegan-Friendly”
“7:00am Fresh Daily Grounded Coffee and Breakfast”

• Call-to-Action: “Order Online at MarlosCorner.com”
• Placeholder for the logo.
• Size: 4.25 x 11 (Door Hanger)
• File Format: High-resolution PDF, JPEG, or PNG.
• Print-Ready: Include bleed margins and ensure print clarity.

6. Tone
• Friendly and professional. Highlighting that your business is women-owned adds a unique and personal touch vs deli meat shops. We are a gourmet sandwich shop, with fresh baked bread, house-made meats, with gluten and vegan options. Each sandwich is made with love.

Target Market(s)

Coffee drinkers for morning crowd and sandwiches for lunch

Industry/Entity Type

Sandwich Shop

Colors
EB3D1F
EC4F4E
F09395
F8D3D4
FCEDEE

Requirements
Must have
• See Description
Nice to have
• Use website to get a feel for color theme
Should not have
• NA

```html
<!DOCTYPE html>
<html lang="en">
<head>
<meta charset="utf-8">
<title>Marlo’s Sandwich Corner – Grand Opening Door Hanger</title>
<link rel="stylesheet" href="https://fonts.googleapis.com/css2?family=Open+Sans:wght@400;600;800&family=Playfair+Display:ital,wght@0,700;0,800;1,700;1,800;1,900&display=swap">
<style>
  :root {
    --stage: #6b6b6b;
    --ink: #111111;
    --black: #0c0c0c;
    --white: #ffffff;
    --orange: #eb3d1f;
    --orange-band: #ee4b22;
    --coral: #ec4f4e;
    --pink-mid: #f09395;
    --pink: #f8d3d4;
    --pink-pale: #fcedee;
  }
  * { box-sizing: border-box; margin: 0; padding: 0; }
  html, body { width: 900px; height: 1200px; overflow: hidden; background: var(--stage); }
  .canvas { position: relative; width: 900px; height: 1200px; background: var(--stage); }

  .door-hanger {
    position: absolute; left: 230px; top: 86px; width: 397px; height: 1027px;
    background: var(--black); overflow: hidden;
    font-family: "Open Sans", Arial, sans-serif; color: var(--ink);
  }
  .door-hanger > * { position: absolute; }

  .pink-field {
    inset: 0;
    background:
      radial-gradient(circle at 200px 480px, var(--pink-pale) 0%, #fbdfe1 45%, var(--pink) 100%);
    clip-path: path("M0,0 H200 C320,55 385,160 397,300 V1002 L380,998 L350,1004 L310,997 L270,1003 L230,996 L190,1004 L150,997 L110,1003 L70,996 L30,1003 L0,998 Z");
  }

  .hang-slot { left: 0; top: 114px; width: 202px; height: 68px; background: var(--stage); }
  .hang-hole { left: 136px; top: 80px; width: 132px; height: 132px; border-radius: 50%; background: var(--stage); }

  .brand-name {
    left: 34px; top: 26px; width: 150px;
    font-family: "Playfair Display", Georgia, serif; font-weight: 800;
    font-size: 21px; line-height: 1; color: var(--orange); text-align: center;
  }

  .headline { font-family: "Playfair Display", Georgia, serif; font-weight: 700; line-height: 1; z-index: 2; }
  .headline-grand { left: 55px; top: 222px; font-size: 33px; color: var(--ink); }
  .headline-opening { left: 14px; top: 248px; font-size: 50px; color: var(--orange); }

  .sandwich-photo {
    left: 0; top: 286px; width: 397px; height: 210px; z-index: 1;
    background: linear-gradient(100deg, #c9a57c 0%, #e7c7a0 25%, #d8352a 45%, #f2e6cc 60%, #8aa84c 75%, #b88d5f 100%);
    clip-path: polygon(0 19%, 30% 15%, 58% 9%, 80% 3%, 100% 0, 100% 86%, 80% 92%, 60% 88%, 40% 95%, 20% 93%, 8% 100%, 0 97%);
  }

  .coffee-badge {
    left: 256px; top: 428px; width: 128px; height: 128px; border-radius: 50%; z-index: 3;
    background: var(--black); border: 5px solid var(--white);
    display: flex; flex-direction: column; align-items: center; justify-content: center;
    text-align: center; color: var(--white);
  }
  .coffee-time { font-weight: 800; font-size: 19px; color: var(--orange); line-height: 1; margin-bottom: 3px; }
  .coffee-note { font-size: 10px; line-height: 1.2; font-weight: 600; }

  .owned-big {
    left: 33px; top: 500px; font-family: "Playfair Display", Georgia, serif;
    font-style: italic; font-weight: 800; font-size: 60px; line-height: 1; color: var(--ink);
  }
  .owned-sub {
    left: 22px; top: 556px; font-family: "Playfair Display", Georgia, serif;
    font-style: italic; font-weight: 700; font-size: 29px; line-height: 1; color: var(--orange);
  }
  .tagline { left: 24px; top: 590px; font-size: 16.5px; font-weight: 600; color: var(--ink); white-space: nowrap; }

  .feature-band {
    left: 0; top: 628px; width: 397px; height: 272px; background: var(--orange-band);
    clip-path: polygon(0 4%, 12% 2%, 30% 3%, 50% 1%, 70% 2%, 88% 0, 100% 1%, 100% 94%, 85% 96%, 65% 93%, 45% 97%, 25% 94%, 8% 98%, 0 96%);
  }
  .band-divider-h { left: 10px; top: 778px; width: 377px; height: 1px; background: rgba(255,255,255,0.35); }
  .band-divider-v { left: 221px; top: 650px; width: 1px; height: 220px; background: rgba(255,255,255,0.35); }

  .feature { width: 200px; text-align: center; color: var(--white); font-size: 13px; line-height: 1.35; font-weight: 600; }
  .feature svg { display: block; margin: 0 auto 10px; }
  .feature-bread { left: 9px; top: 676px; }
  .feature-roast { left: 204px; top: 656px; }
  .feature-gluten { left: 9px; top: 787px; }
  .feature-vegan { left: 204px; top: 785px; }

  .order-label { left: 0; width: 397px; top: 888px; text-align: center; font-size: 23px; color: var(--ink); }
  .order-url {
    left: 0; width: 397px; top: 912px; text-align: center;
    font-family: "Playfair Display", Georgia, serif; font-style: italic; font-weight: 700; font-size: 37px; color: var(--orange);
  }
</style>
</head>
<body>
<main class="canvas">
  <article class="door-hanger">
    <div class="pink-field"></div>
    <div class="hang-slot"></div>
    <div class="hang-hole"></div>

    <div class="brand-name">Marlo’s Sandwich Corner</div>

    <div class="sandwich-photo" role="img" aria-label="Photo of grilled panini halves with tomato, basil, lettuce and melted cheese"></div>

    <h1 class="headline headline-grand">Grand</h1>
    <div class="headline headline-opening">Opening</div>

    <div class="coffee-badge">
      <div class="coffee-time">7:00am</div>
      <div class="coffee-note">Fresh Daily Grounded<br>Coffee<br>and Breakfast</div>
    </div>

    <div class="owned-big">women</div>
    <div class="owned-sub">and family owned</div>
    <p class="tagline">Handcrafted Sandwiches Made with Love</p>

    <div class="feature-band"></div>
    <div class="band-divider-h"></div>
    <div class="band-divider-v"></div>

    <div class="feature feature-bread">
      <svg width="52" height="44" viewBox="0 0 52 44" fill="none" stroke="#fff" stroke-width="2.2" stroke-linecap="round">
        <path d="M20 4c-3 3 3 5 0 9M26 2c-3 3 3 5 0 9M32 4c-3 3 3 5 0 9"/>
        <path d="M6 28c4-10 36-10 40 0"/>
        <path d="M4 28h44v4H4z" fill="#fff"/>
        <path d="M8 32l3 8h30l3-8"/>
        <path d="M18 23l4-2M28 22l4 1"/>
      </svg>
      Fresh Baked Breadrafted<br>Sandwiches Made with Love
    </div>

    <div class="feature feature-roast">
      <svg width="54" height="46" viewBox="0 0 54 46" fill="none" stroke="#fff" stroke-width="2.2" stroke-linecap="round" stroke-linejoin="round">
        <path d="M22 4c-2 2 2 4 0 6M30 4c-2 2 2 4 0 6"/>
        <path d="M12 24l15-11 15 11"/>
        <path d="M4 26h46"/>
        <path d="M9 26v12a4 4 0 0 0 4 4h28a4 4 0 0 0 4-4V26"/>
        <rect x="24" y="29" width="6" height="6"/>
      </svg>
      House-made Slow<br>Roasted House<br>Specialties
    </div>

    <div class="feature feature-gluten">
      <svg width="40" height="40" viewBox="0 0 40 40" fill="none" stroke="#fff" stroke-width="2.2" stroke-linecap="round">
        <circle cx="20" cy="20" r="17"/>
        <path d="M20 10v22M20 15c-4 0-5-3-5-5 3 0 5 2 5 5zM20 15c4 0 5-3 5-5-3 0-5 2-5 5zM20 21c-4 0-5-3-5-5 3 0 5 2 5 5zM20 21c4 0 5-3 5-5-3 0-5 2-5 5z"/>
        <path d="M8 8l24 24"/>
      </svg>
      Gluten-Friendly
    </div>

    <div class="feature feature-vegan">
      <svg width="40" height="40" viewBox="0 0 40 40" fill="#fff">
        <path d="M36 4C20 4 8 10 8 24c0 4 2 7 4 9 2-10 9-17 18-21-7 5-13 12-15 23 2 1 4 1 6 1 13 0 15-16 15-32z"/>
      </svg>
      Vegan-Friendly
    </div>

    <p class="order-label">Order Online at</p>
    <p class="order-url">MarlosCorner.com</p>
  </article>
</main>
</body>
</html>
```